Forensic Document Examiner, looking for contemporary update to my stationery design.

Looking for professional, classy logo design for stationery and business cards. My current stationery and business card is attached.I believe a logo image makes a header section interesting, so an intriguing design of a pen, feathered pen, microscope, magnifying glass, etc., would be appropriate. I have been in the business for over 30 years. I leave ideas to the imagination of the designer.My work involves mainly, the comparison of signatures and handwriting. I also resolve alterations, obliterations, and work as shown on my website: www.documentexaminer.infoThe image produced will be printed on quality white stationery and envelopes. The stationery will be photocopied by my clients, so the images should be reproducible. The business cards may be designed in other than white.

Target Market(s)

Attorneys

Font styles to use
Sans Serif

Colors

Designer to choose colors to be used in the design.

Requirements
Must have
• Image suitable for white stationery and photocopying.
• Classy logo and image; no casual fonts.
Nice to have
• Intriguing, contemporary design incorporating a relevant logo to my work.

```html
<!DOCTYPE html>
<html lang="en">
<head>
<meta charset="utf-8">
<title>Martin R. Hale — Business Card</title>
<link href="https://fonts.googleapis.com/css2?family=PT+Serif:ital,wght@0,400;0,700;1,400&display=swap" rel="stylesheet">
<style>
  :root {
    --bg: #1c2036;
    --indigo: #2f2a78;
    --indigo-deep: #241f63;
    --indigo-light: #3d3791;
    --yellow: #f4cf1c;
    --ink-grey: #8a8a93;
    --rule-grey: #d6d6da;
    --paper: #ffffff;
  }
  * { box-sizing: border-box; margin: 0; padding: 0; }
  html, body { width: 1200px; height: 900px; overflow: hidden; }
  body {
    background: var(--bg);
    font-family: "PT Serif", Georgia, serif;
    display: flex;
    flex-direction: column;
    align-items: center;
    justify-content: center;
    gap: 44px;
  }
  .card {
    position: relative;
    width: 700px;
    height: 400px;
    border-radius: 30px;
    overflow: hidden;
  }

  /* Front */
  .card-front { background: var(--paper); }
  .card-front .edge-accent { position: absolute; inset: 0; }
  .brand {
    position: absolute;
    left: 150px;
    top: 48px;
    display: flex;
    align-items: center;
    gap: 18px;
  }
  .brand-dot {
    width: 58px; height: 58px; border-radius: 50%;
    background: var(--rule-grey);
  }
  .brand-name {
    color: var(--indigo);
    font-weight: 700;
    font-size: 34px;
    line-height: 1.05;
  }
  .brand-title {
    color: var(--ink-grey);
    font-size: 15px;
    margin-top: 4px;
  }
  .tagline {
    position: absolute;
    left: 60px;
    top: 236px;
    width: 440px;
    color: var(--indigo);
    font-size: 19px;
    line-height: 1.45;
  }
  .divider {
    position: absolute;
    left: 0; top: 0;
  }
  .contact-list {
    position: absolute;
    left: 455px;
    top: 96px;
    list-style: none;
    display: flex;
    flex-direction: column;
    gap: 10px;
  }
  .contact-item {
    display: flex;
    align-items: center;
    gap: 10px;
    font-size: 15px;
    color: var(--ink-grey);
  }
  .contact-item.primary { color: var(--indigo); font-weight: 700; }
  .contact-icon { width: 16px; height: 16px; flex: none; }

  /* Back */
  .card-back {
    background: linear-gradient(135deg, var(--indigo-light) 0%, var(--indigo) 55%, var(--indigo-deep) 100%);
    color: #fff;
  }
  .back-brand {
    position: absolute;
    left: 150px;
    top: 120px;
    display: flex;
    align-items: center;
    gap: 30px;
  }
  .back-dot {
    width: 120px; height: 120px; border-radius: 50%;
    background: #dcdce2;
  }
  .back-name { font-weight: 700; font-size: 56px; line-height: 1; }
  .back-title { font-size: 24px; margin-top: 10px; color: #e6e4f5; }
</style>
</head>
<body>

<section class="card card-front" aria-label="Business card front">
  <svg class="edge-accent" width="700" height="400" viewBox="0 0 700 400" aria-hidden="true">
    <path d="M0 150 L0 400 L40 400 Z" fill="var(--indigo)"/>
    <line x1="14" y1="200" x2="60" y2="400" stroke="var(--yellow)" stroke-width="4"/>
    <rect x="0" y="372" width="120" height="28" fill="var(--yellow)"/>
    <rect x="0" y="372" width="60" height="28" fill="var(--indigo)"/>
    <line x1="6" y1="120" x2="6" y2="240" stroke="var(--indigo)" stroke-width="4"/>
  </svg>

  <div class="brand">
    <div class="brand-dot"></div>
    <div>
      <div class="brand-name">Martin R.Hale</div>
      <div class="brand-title">Forensic Document Examinar</div>
    </div>
  </div>

  <svg class="divider" width="700" height="400" viewBox="0 0 700 400" aria-hidden="true">
    <line x1="425" y1="60" x2="425" y2="220" stroke="var(--rule-grey)" stroke-width="2"/>
  </svg>

  <ul class="contact-list">
    <li class="contact-item primary">
      <svg class="contact-icon" viewBox="0 0 16 16" aria-hidden="true"><circle cx="8" cy="8" r="8" fill="var(--yellow)"/><path d="M8 3.5a3 3 0 0 0-3 3c0 2.2 3 6 3 6s3-3.8 3-6a3 3 0 0 0-3-3z" fill="#fff"/></svg>
      PO Box 2841 Linden, OR 97330
    </li>
    <li class="contact-item">
      <svg class="contact-icon" viewBox="0 0 16 16" aria-hidden="true"><circle cx="8" cy="8" r="8" fill="var(--yellow)"/><path d="M5 4h2l1 2.3-1.2.9a5 5 0 0 0 2 2l.9-1.2L12 9v2a1 1 0 0 1-1 1A7 7 0 0 1 4 5a1 1 0 0 1 1-1z" fill="#fff"/></svg>
      555-201-7734
    </li>
    <li class="contact-item">
      <svg class="contact-icon" viewBox="0 0 16 16" aria-hidden="true"><circle cx="8" cy="8" r="8" fill="var(--yellow)"/><rect x="4" y="5" width="8" height="6" fill="#fff"/><path d="M4 5l4 3.2L12 5" stroke="var(--yellow)" fill="none"/></svg>
      mhale@quillverity.example
    </li>
    <li class="contact-item">
      <svg class="contact-icon" viewBox="0 0 16 16" aria-hidden="true"><circle cx="8" cy="8" r="8" fill="var(--yellow)"/><circle cx="8" cy="8" r="4" fill="none" stroke="#fff" stroke-width="1.2"/><line x1="4" y1="8" x2="12" y2="8" stroke="#fff" stroke-width="1"/></svg>
      www.quillverity.example
    </li>
  </ul>

  <p class="tagline">Full service laboratory specializing in handwriting comparisons, obliterations, alterations, indented writing recovery etc.</p>
</section>

<section class="card card-back" aria-label="Business card back">
  <div class="back-brand">
    <div class="back-dot"></div>
    <div>
      <div class="back-name">Martin R.Hale</div>
      <div class="back-title">Forensic Document Examinar</div>
    </div>
  </div>
</section>

</body>
</html>
```